Business Card Design Project

Use our current logo. Clean design.

Industry/Entity Type

Business

Requirements
Must have
• Marisela DUBRANCQ
M. Law
Managing Partner

Alpenvorsa AG
Kornhalmweg 214
CH-3097 Liebefeld

M. +41 79 412 56 27
T. +41 31 928 44 10
F. +41 31 928 44 19

m.dubrancq@alpenvorsa-example.com
www.alpenvorsa-example.com

```html
<!DOCTYPE html>
<html lang="en">
<head>
<meta charset="utf-8">
<title>Alpenvorsa AG – Business Card</title>
<link href="https://fonts.googleapis.com/css2?family=Open+Sans:wght@400;600&display=swap" rel="stylesheet">
<style>
  :root {
    --page-bg: #ececea;
    --card-dark: #141414;
    --card-mid: #2c2c2c;
    --grid-line: rgba(255,255,255,0.055);
    --ink: #ffffff;
    --ink-soft: #d8d8d8;
  }
  * { box-sizing: border-box; margin: 0; padding: 0; }
  html, body {
    width: 1200px; height: 1049px; overflow: hidden;
    background: var(--page-bg);
  }
  .stage { position: relative; width: 1200px; height: 1049px; }

  .card {
    position: absolute;
    width: 600px; height: 343px;
    background:
      linear-gradient(var(--grid-line) 1px, transparent 1px) 0 0 / 22px 22px,
      linear-gradient(90deg, var(--grid-line) 1px, transparent 1px) 0 0 / 22px 22px,
      radial-gradient(ellipse at 50% 35%, var(--card-mid), var(--card-dark) 75%);
    box-shadow: 0 30px 40px rgba(0,0,0,0.28), 0 6px 12px rgba(0,0,0,0.2);
    color: var(--ink);
    font-family: "Open Sans", Arial, sans-serif;
  }
  .card--front { left: 70px; top: 110px; }
  .card--back  { left: 530px; top: 580px; }

  .brand-name {
    font-family: "Open Sans", Arial, sans-serif;
    font-weight: 600;
    color: var(--ink);
    letter-spacing: 0.06em;
    text-align: center;
  }

  /* Front */
  .front-brand { position: absolute; top: 52px; left: 0; right: 0; font-size: 24px; }
  .holder { position: absolute; top: 112px; left: 0; right: 0; text-align: center; }
  .holder-name { font-size: 18px; font-weight: 600; letter-spacing: 0.04em; }
  .holder-role { font-size: 12px; color: var(--ink-soft); line-height: 1.45; margin-top: 4px; }

  .address {
    position: absolute; left: 34px; bottom: 34px;
    font-size: 11px; line-height: 1.45; color: var(--ink-soft); font-style: normal;
  }
  .address .phones { margin-top: 12px; }
  .web {
    position: absolute; right: 30px; top: 190px;
    font-size: 10.5px; line-height: 1.45; color: var(--ink-soft); text-align: right;
  }

  /* Back */
  .back-brand {
    position: absolute; top: 146px; left: 0; right: 0;
    font-size: 40px;
  }
</style>
</head>
<body>
<main class="stage">

  <section class="card card--front" aria-label="Business card front">
    <div class="brand-name front-brand">ALPENVORSA</div>
    <div class="holder">
      <p class="holder-name">MARISELA DUBRANCQ</p>
      <p class="holder-role">M. Law<br>Managing Partner</p>
    </div>
    <address class="address">
      Alpenvorsa AG<br>
      Kornhalmweg 214<br>
      CH-3097 Liebefeld
      <div class="phones">
        M : +41 79 412 56 27<br>
        T : +41 31 928 44 10<br>
        F : +41 31 928 44 19
      </div>
    </address>
    <div class="web">
      m.dubrancq@alpenvorsa-example.com<br>
      www.alpenvorsa-example.com
    </div>
  </section>

  <section class="card card--back" aria-label="Business card back">
    <div class="brand-name back-brand">ALPENVORSA</div>
  </section>

</main>
</body>
</html>
```